Sandwich Board and Poster design promoting a medical aesthetic clinic

I am looking for a clean, modern and relaxing design promoting a medical physician-led aesthetic clinic.
Services offered are neuromodulator treatment (Velmira) and Dermal Fillers.
Logo must be included.
Use the tag line "Refresh your look, revive your spirit."
Address is 204-205 27391 83 Ave, Surrey, V2K 4N7
604-718-2453
email - info@glowmapleco.ca
www.glowmapleco.ca

```html
<!DOCTYPE html>
<html lang="en">
<head>
<meta charset="utf-8">
<title>Glow Maple – Medical Aesthetics Poster</title>
<link href="https://fonts.googleapis.com/css2?family=Josefin+Sans:ital,wght@0,300;0,400;0,600;1,400&display=swap" rel="stylesheet">
<style>
  :root {
    --backdrop: #3b3a3b;
    --ink: #1c1a19;
    --gold: #a8862a;
    --veil: rgba(255, 255, 255, 0.62);
    --veil-soft: rgba(255, 255, 255, 0.5);
    --white: #ffffff;
  }
  * { margin: 0; padding: 0; box-sizing: border-box; }
  html, body {
    width: 1200px; height: 1200px; overflow: hidden;
    background: var(--backdrop);
    font-family: "Josefin Sans", sans-serif;
    color: var(--ink);
  }
  .poster {
    position: absolute; left: 214px; top: 20px;
    width: 772px; height: 1160px; overflow: hidden;
  }
  .photo {
    position: absolute; inset: 0;
    background:
      linear-gradient(90deg, rgba(90,60,40,0.35) 0%, rgba(0,0,0,0) 35%, rgba(0,0,0,0) 75%, rgba(235,215,200,0.3) 100%),
      linear-gradient(180deg, #e9f1f5 0%, #f0e6e0 18%, #d9a184 34%, #c98a6a 48%, #a8735a 62%, #d9c2b4 74%, #8a6a55 88%, #4a3326 100%);
  }
  .band { position: absolute; left: 0; width: 100%; }
  .band--header { top: 0; height: 226px; background: var(--veil); }
  .side { position: absolute; top: 226px; height: 372px; width: 120px; background: var(--veil-soft); }
  .side--left { left: 0; }
  .side--right { right: 0; }
  .band--services { top: 602px; height: 337px; background: rgba(250, 244, 240, 0.72); }
  .band--contact { top: 944px; height: 134px; background: rgba(240, 236, 233, 0.66); text-align: center; }
  .band--tagline { top: 1078px; height: 82px; }

  .brand {
    position: absolute; top: 150px; width: 100%; text-align: center;
    font-size: 28px; font-weight: 400; letter-spacing: 0.3em; color: var(--ink);
  }
  .headline {
    position: absolute; left: 81px; top: 654px;
    font-size: 54px; font-weight: 300; letter-spacing: 0.04em; line-height: 1;
    white-space: nowrap; color: var(--ink);
  }
  .service { position: absolute; top: 760px; }
  .service--left { left: 81px; }
  .service--right { left: 401px; }
  .service h2 {
    font-size: 23px; font-weight: 400; color: var(--gold); letter-spacing: 0.03em; margin-bottom: 8px;
  }
  .service ul { list-style: none; font-size: 18px; font-weight: 300; }
  .service li { line-height: 27px; }
  .service li::before { content: "•"; margin-right: 8px; font-size: 12px; vertical-align: 2px; }

  .contact-name { margin-top: 26px; font-size: 21px; font-weight: 600; }
  .contact-address { margin-top: 8px; font-size: 19px; font-weight: 300; }
  .contact-lines { margin-top: 8px; font-size: 19px; font-weight: 300; }
  .contact-lines span + span::before { content: "•"; margin: 0 8px; }

  .tagline {
    padding-top: 30px; text-align: center; color: var(--white);
    font-size: 21px; font-style: italic; font-weight: 400; letter-spacing: 0.04em;
  }
</style>
</head>
<body>
  <main class="poster">
    <div class="photo" role="img" aria-label="Photograph of a gloved practitioner giving a cosmetic injection near a client's temple"></div>

    <section class="band band--header">
      <p class="brand">GLOW MAPLE</p>
    </section>
    <div class="side side--left"></div>
    <div class="side side--right"></div>

    <section class="band band--services"></section>
    <h1 class="headline">MEDICAL AESTHETICS</h1>
    <div class="service service--left">
      <h2>VELMIRA</h2>
      <ul>
        <li>Fine Lines &amp; Wrinkles</li>
        <li>TMJ</li>
        <li>Chronic Migraines</li>
        <li>Hyperhidrosis</li>
      </ul>
    </div>
    <div class="service service--right">
      <h2>DERMAL FILLERS</h2>
      <ul>
        <li>Lip Enhancements</li>
        <li>Sunken/Hollow Eyes</li>
        <li>Sagging Skin</li>
        <li>Chin &amp; Cheek Structuring</li>
      </ul>
    </div>

    <section class="band band--contact">
      <p class="contact-name">Dr. Arveen Dhaliwal, BSc, MBChB, CCFP</p>
      <p class="contact-address">204-205 27391 83 Ave, Surrey, V2K 4N7</p>
      <p class="contact-lines"><span>604-718-2453</span><span>info@glowmapleco.ca</span><span>www.glowmapleco.ca</span></p>
    </section>

    <section class="band band--tagline">
      <p class="tagline">REFRESH YOUR LOOK, REVIVE YOUR SPIRIT.</p>
    </section>
  </main>
</body>
</html>
```